Business Card Design for Venture Kite

Venture Kite is a pro bono student consultancy service offered by Corvala KTRB to social start ups and enterprises. We provide consulting services with expertise in areas such as Marketing, IT, Business Strategy and Innovation.
I have attached\ the Venture Kite Logo here for your perusal.
Industry/Entity Type
Business
Contact Information for Business Card
Name: Ha Min Park Name: Thomas Leung
Role: Project Leader Role: Vice Project Leader
M:0477203941 M: 0479352806
E: ha-min.park@corvalaktrb.org E: thomas.leung@corvalaktrb.org
W: www.corvalaktrb.org W: www.corvalaktrb.org

```html
<!DOCTYPE html>
<html lang="en">
<head>
<meta charset="utf-8">
<title>Venture Kite – Business Cards</title>
<link href="https://fonts.googleapis.com/css2?family=PT+Sans+Narrow:wght@400;700&family=Open+Sans:wght@400;600&display=swap" rel="stylesheet">
<style>
  :root {
    --backdrop: #3b3b3d;
    --card-white: #ffffff;
    --card-shade: #e9e9e9;
    --orange: #e38a12;
    --orange-deep: #bf6408;
    --pill: rgba(120, 58, 0, 0.42);
    --ink: #111111;
    --ink-soft: #222222;
  }
  * { margin: 0; padding: 0; box-sizing: border-box; }
  html, body { width: 1200px; height: 800px; overflow: hidden; }
  body {
    background: var(--backdrop);
    position: relative;
    font-family: "Open Sans", sans-serif;
  }
  .card {
    position: absolute;
    width: 500px;
    height: 285px;
    background: var(--card-white);
    overflow: hidden;
    box-shadow: 0 10px 24px rgba(0,0,0,0.45);
  }
  .card--ha { left: 60px; top: 60px; }
  .card--thomas { left: 640px; top: 60px; }
  .card--back {
    left: 350px; top: 450px;
    background: radial-gradient(ellipse at 50% 40%, var(--card-white) 45%, var(--card-shade) 100%);
  }
  .card__wave { position: absolute; inset: 0; width: 100%; height: 100%; }
  .wordmark {
    position: absolute;
    font-family: "PT Sans Narrow", sans-serif;
    font-weight: 700;
    color: var(--ink);
    text-transform: uppercase;
    line-height: 1;
    letter-spacing: 0.5px;
  }
  .card--ha .wordmark, .card--thomas .wordmark { left: 40px; top: 40px; font-size: 46px; }
  .card--back .wordmark {
    left: 0; right: 0; top: 100px;
    text-align: center; font-size: 62px;
  }
  .holder {
    position: absolute;
    right: 46px;
    top: 110px;
    text-align: left;
  }
  .holder__name {
    font-family: "PT Sans Narrow", sans-serif;
    font-weight: 400;
    font-size: 30px;
    color: var(--orange);
    line-height: 1.1;
  }
  .holder__role {
    font-family: "Open Sans", sans-serif;
    font-weight: 600;
    font-size: 13px;
    color: var(--ink-soft);
    text-transform: uppercase;
    letter-spacing: 0.3px;
    margin-top: 4px;
  }
  .contacts {
    position: absolute;
    left: 32px;
    top: 190px;
    list-style: none;
  }
  .contacts__item {
    display: flex;
    align-items: center;
    gap: 9px;
    width: max-content;
    padding: 3px 16px 3px 10px;
    margin-bottom: 6px;
    border-radius: 12px;
    background: var(--pill);
    color: var(--card-white);
    font-size: 13px;
    line-height: 18px;
  }
  .contacts__icon { width: 13px; height: 13px; flex: none; }
  .card__band {
    position: absolute;
    left: 0; right: 0; bottom: 0;
    height: 26px;
    background: var(--orange);
  }
</style>
</head>
<body>

  <section class="card card--ha">
    <svg class="card__wave" viewBox="0 0 500 285" preserveAspectRatio="none" aria-hidden="true">
      <path d="M0 140 C110 112 200 140 300 170 C380 192 440 160 500 108 L500 285 L0 285 Z" fill="var(--orange-deep)"/>
      <path d="M0 158 C110 130 200 150 300 180 C380 200 445 170 500 128 L500 285 L0 285 Z" fill="var(--orange)"/>
    </svg>
    <div class="wordmark">Venture Kite</div>
    <div class="holder">
      <div class="holder__name">Ha Min Park</div>
      <div class="holder__role">Project Leader</div>
    </div>
    <ul class="contacts">
      <li class="contacts__item">
        <svg class="contacts__icon" viewBox="0 0 16 16"><rect x="4" y="1" width="8" height="14" rx="1.5" fill="none" stroke="#fff" stroke-width="1.6"/><rect x="6" y="3.5" width="4" height="6" fill="#fff"/></svg>
        0477203941
      </li>
      <li class="contacts__item">
        <svg class="contacts__icon" viewBox="0 0 16 16"><rect x="1" y="3" width="14" height="10" rx="1" fill="#fff"/><path d="M1 4 L8 9 L15 4" fill="none" stroke="#8a4a06" stroke-width="1.4"/></svg>
        ha-min.park@corvalaktrb.org
      </li>
      <li class="contacts__item">
        <svg class="contacts__icon" viewBox="0 0 16 16" fill="none" stroke="#fff" stroke-width="1.4"><circle cx="8" cy="8" r="6.5"/><ellipse cx="8" cy="8" rx="3" ry="6.5"/><path d="M1.5 8 H14.5"/></svg>
        www.corvalaktrb.org
      </li>
    </ul>
  </section>

  <section class="card card--thomas">
    <svg class="card__wave" viewBox="0 0 500 285" preserveAspectRatio="none" aria-hidden="true">
      <path d="M0 140 C110 112 200 140 300 170 C380 192 440 160 500 108 L500 285 L0 285 Z" fill="var(--orange-deep)"/>
      <path d="M0 158 C110 130 200 150 300 180 C380 200 445 170 500 128 L500 285 L0 285 Z" fill="var(--orange)"/>
    </svg>
    <div class="wordmark">Venture Kite</div>
    <div class="holder">
      <div class="holder__name">Thomas Leung</div>
      <div class="holder__role">Vice Project Leader</div>
    </div>
    <ul class="contacts">
      <li class="contacts__item">
        <svg class="contacts__icon" viewBox="0 0 16 16"><rect x="4" y="1" width="8" height="14" rx="1.5" fill="none" stroke="#fff" stroke-width="1.6"/><rect x="6" y="3.5" width="4" height="6" fill="#fff"/></svg>
        0479352806
      </li>
      <li class="contacts__item">
        <svg class="contacts__icon" viewBox="0 0 16 16"><rect x="1" y="3" width="14" height="10" rx="1" fill="#fff"/><path d="M1 4 L8 9 L15 4" fill="none" stroke="#8a4a06" stroke-width="1.4"/></svg>
        thomas.leung@corvalaktrb.org
      </li>
      <li class="contacts__item">
        <svg class="contacts__icon" viewBox="0 0 16 16" fill="none" stroke="#fff" stroke-width="1.4"><circle cx="8" cy="8" r="6.5"/><ellipse cx="8" cy="8" rx="3" ry="6.5"/><path d="M1.5 8 H14.5"/></svg>
        www.corvalaktrb.org
      </li>
    </ul>
  </section>

  <section class="card card--back">
    <div class="wordmark">Venture Kite</div>
    <div class="card__band"></div>
  </section>

</body>
</html>
```